International professional tennis coach needs a book cover design

This is my 2nd published book, the first one was a #1 on the best seller. I'm looking for a world class book cover design for this new book. The name of my first book was 5 Baseline Habits to Unlock Your Flow Zone, located on Brimlow.com

The title of the new book:

Title: The Craft of Rally Mastery
Subtitle: Developing a Strategic Advantage through Competitive Intelligence

I'm uploading our new CRAFT OF RALLY logo that I'd like for you to use as the centerpiece of the book design along with a 21st century design feel that incorporates what the book topic is below::

--> This book is about building competitive intelligence by using tennis data analytics to develop and expand a player's strategic advantage for match play. <--

The colors we would like to use are Blue, Yellow, and Green. These shades of these colors should be bold! (You will see the bold color examples of blues, yellows, and greens that I'm talking about in the logos that are attached here, especially the colors for my Racquet GridLoop App logo.

I will upload the Racquet GridLoop logo which should go somewhere on the back cover design (small size maybe in the bottom corner).

This book is revolutionary to the standard way of teaching tennis, it is based on a decade of recording and gathering tennis data analytics and then we created on-court practice games to develop better decision making in players for the competitive edge.

My websites are www.elevatedrillyard.example and www.craftofrallymastery.example

```html
<!DOCTYPE html>
<html lang="en">
<head>
<meta charset="utf-8">
<title>The Craft of Rally Mastery — Book Cover</title>
<link rel="stylesheet" href="https://fonts.googleapis.com/css2?family=Montserrat:wght@400;500;800;900&display=swap">
<style>
  :root {
    --backdrop: #262626;
    --paper: #ffffff;
    --ink: #262626;
    --green: #93c43d;
    --lime: #c7da2a;
    --blue: #1f6fb8;
    --sky: #3fa9e0;
  }
  html, body {
    margin: 0;
    width: 1200px;
    height: 1200px;
    overflow: hidden;
    background: var(--backdrop);
  }
  .book-cover {
    position: absolute;
    left: 237px;
    top: 53px;
    width: 728px;
    height: 1092px;
    background: var(--paper);
    box-shadow: 0 10px 40px rgba(0,0,0,0.45);
    font-family: "Montserrat", sans-serif;
  }
  .subtitle {
    position: absolute;
    top: 42px;
    left: 0;
    width: 100%;
    margin: 0;
    text-align: center;
    font-weight: 500;
    font-size: 29px;
    line-height: 43px;
    letter-spacing: 0.6px;
    color: var(--ink);
  }
  .brand-mark {
    position: absolute;
    top: 218px;
    left: 50%;
    width: 150px;
    height: 150px;
    margin-left: -75px;
    border-radius: 50%;
    background: linear-gradient(160deg, var(--sky), var(--blue));
  }
  .brand-name {
    position: absolute;
    top: 482px;
    left: 0;
    width: 100%;
    margin: 0;
    text-align: center;
    font-weight: 800;
    font-size: 40px;
    letter-spacing: 1px;
    color: var(--green);
  }
  .divider {
    position: absolute;
    top: 589px;
    left: 104px;
    width: 519px;
    height: 4px;
    border-radius: 50%;
    background: var(--green);
  }
  .book-title {
    position: absolute;
    top: 610px;
    left: 0;
    width: 728px;
    height: 370px;
  }
  .book-title text {
    font-family: "Montserrat", sans-serif;
  }
  .author-band {
    position: absolute;
    left: 0;
    bottom: 0;
    width: 100%;
    height: 78px;
    background: var(--green);
    display: flex;
    align-items: center;
    justify-content: center;
  }
  .author-name {
    margin: 0;
    font-weight: 500;
    font-size: 46px;
    letter-spacing: 6px;
    color: var(--paper);
  }
</style>
</head>
<body>
  <main class="book-cover">
    <p class="subtitle">Developing a Strategic Advantage<br>Through Competitive Intelligence</p>

    <div class="brand-mark" aria-hidden="true"></div>
    <p class="brand-name">Racquet GridLoop</p>

    <div class="divider"></div>

    <svg class="book-title" viewBox="0 0 728 370" role="img" aria-label="The Craft of Rally Mastery">
      <defs>
        <linearGradient id="title-green" x1="0" y1="0" x2="0" y2="1">
          <stop offset="0" stop-color="var(--lime)"/>
          <stop offset="1" stop-color="var(--green)"/>
        </linearGradient>
        <linearGradient id="title-blue" x1="0" y1="0" x2="0" y2="1">
          <stop offset="0" stop-color="var(--sky)"/>
          <stop offset="1" stop-color="var(--blue)"/>
        </linearGradient>
      </defs>
      <text x="364" y="79" text-anchor="middle" font-weight="800" font-size="84"
            fill="var(--ink)" textLength="530" lengthAdjust="spacingAndGlyphs">THE CRAFT OF</text>
      <text x="364" y="198" text-anchor="middle" font-weight="900" font-size="136"
            fill="url(#title-green)" textLength="630" lengthAdjust="spacingAndGlyphs">RALLY</text>
      <text x="364" y="352" text-anchor="middle" font-weight="900" font-size="178"
            fill="url(#title-blue)" textLength="630" lengthAdjust="spacingAndGlyphs">MASTERY</text>
    </svg>

    <footer class="author-band">
      <p class="author-name">DORIAN VALECOURT</p>
    </footer>
  </main>
</body>
</html>
```